Website for Party

Design a new website for PlumtreeGatherings.net
We have attached the new logos and please look at the website, and our facebook page: facebook.com/plumtreegatherings for inspiration
Updates

Hi Guys, please be original with all designs and images otherwise the design will be eliminated Thank you

some of your designs have too much happening in them, others make it clear that the designer has not yet read the brief fully

Please everyone be original!

```html
<!DOCTYPE html>
<html lang="en">
<head>
<meta charset="utf-8">
<title>Plumtree Gatherings — July 4th Party</title>
<link rel="stylesheet" href="https://fonts.googleapis.com/css2?family=Open+Sans:wght@400;700;800&family=Londrina+Solid:wght@900&family=Michroma&family=Questrial&family=Montserrat:wght@600;700&display=swap">
<style>
:root{
  --black:#050303;
  --nav:#3b3b3b;
  --nav-active:#151515;
  --yellow:#f2e600;
  --gold:#e8b400;
  --violet:#b400ff;
  --sky:#29a9ff;
  --white:#ffffff;
  --cal:#8f8cff;
  --frame:#2c2c2e;
  --footer:#1d1d1d;
  --footer-line:#2b2350;
  --copyright:#e01d1d;
}
*{margin:0;padding:0;box-sizing:border-box}
html,body{width:1200px;height:855px;overflow:hidden;background:var(--black)}
body{position:relative;font-family:"Open Sans",Arial,sans-serif;color:var(--white)}
.backdrop{position:absolute;left:0;top:0;width:1200px;height:812px;
  background:
   linear-gradient(to bottom,transparent 0,transparent 62%,rgba(8,0,2,.55) 80%,rgba(5,0,1,.8) 100%),
   radial-gradient(circle at 530px 300px,#ff9a2a 0,#e2561a 70px,rgba(160,30,20,.6) 135px,transparent 180px),
   radial-gradient(ellipse 260px 170px at 560px 720px,rgba(245,190,30,.75) 0,rgba(220,70,20,.45) 140px,transparent 260px),
   radial-gradient(ellipse 140px 140px at 1000px 540px,rgba(170,25,35,.7) 0,transparent 140px),
   radial-gradient(ellipse 200px 120px at 180px 620px,rgba(120,20,30,.5) 0,transparent 200px),
   radial-gradient(ellipse at 600px 420px,#4a0c12 0,#2a0508 500px,#120204 800px)}
.topbar{position:absolute;left:0;top:0;width:1200px;height:45px;background:#000}
.navbar{position:absolute;left:0;top:45px;width:1200px;height:55px;background:linear-gradient(#4a4a4a,#2c2c2c)}
.brand{position:absolute;left:195px;top:0;width:89px;height:100px;background:#000;display:flex;flex-direction:column;align-items:center;justify-content:center;gap:6px}
.brand-mark{width:22px;height:22px;border-radius:50%;background:var(--white)}
.brand-name{font-family:"Questrial",sans-serif;font-size:11px;line-height:1.15;text-align:center;letter-spacing:1px}
.menu{position:absolute;left:528px;top:45px;height:55px;display:flex;list-style:none;background:var(--nav)}
.menu li{font-family:"Questrial",sans-serif;font-size:14px;line-height:57px;padding:0 20px}
.menu .current{background:var(--nav-active);border-top:2px solid var(--yellow);line-height:55px;position:relative}
.menu .current::after{content:"";position:absolute;right:0;bottom:0;border-left:6px solid transparent;border-bottom:6px solid var(--yellow)}
.headline{position:absolute;left:192px;top:172px;font-family:"Londrina Solid",sans-serif;font-weight:900;font-size:46px;line-height:53px;letter-spacing:-1px}
.headline .l1{color:var(--yellow)}
.headline .l2{color:var(--violet)}.headline .l2 b{color:var(--sky);font-weight:900}
.headline sup{font-size:22px}
.swoosh{position:absolute;left:300px;top:300px}
.ship{position:absolute;left:505px;top:160px;width:505px;height:200px;border-radius:50%;
  background:radial-gradient(ellipse at 55% 50%,#e4eeff 0,#9ab8f4 30%,#5d74d0 52%,rgba(90,70,170,.55) 64%,transparent 72%)}
.departure{position:absolute;left:197px;top:360px;width:321px;height:33px;background:rgba(20,10,10,.85);border-left:4px solid var(--gold);font-size:15px;line-height:33px;padding-left:10px}
.perks{position:absolute;left:197px;top:395px;width:596px;height:28px;background:rgba(20,10,10,.85);border-left:4px solid var(--gold);font-family:"Michroma",sans-serif;font-size:12px;letter-spacing:.6px;color:var(--yellow);line-height:28px;padding-left:9px;white-space:nowrap}
.perks span{margin:0 20px}
.read-more{position:absolute;left:200px;top:426px;width:84px;height:20px;background:#000;font-size:10px;line-height:20px;padding-left:7px;clip-path:polygon(0 0,78% 0,100% 100%,0 100%)}
.pager{position:absolute;left:944px;top:403px;display:flex;gap:4px}
.pager i{width:11px;height:11px;border-radius:50%;background:#777}
.pager i:first-child{background:var(--white)}
.collage{position:absolute;left:0;top:0}
.calendar{position:absolute;left:847px;top:507px;width:160px}
.calendar h3{background:#000;font-size:14px;font-weight:400;height:25px;line-height:25px;padding-left:16px}
.calendar .month{font-family:"Montserrat",sans-serif;font-weight:700;color:var(--cal);font-size:29px;text-align:center;margin:0 0 2px -10px;line-height:40px}
.days{display:grid;grid-template-columns:repeat(7,24px);font-family:"Montserrat",sans-serif;font-weight:700;color:var(--cal);font-size:11px;text-align:center;margin-left:-4px}
.days .head{font-size:19px;line-height:24px}
.days span{line-height:19.7px;height:19.7px}
.days .mark{display:block;border:2px solid var(--gold);border-radius:50%;width:21px;height:21px;line-height:17px;margin:-1px auto 0}
.features{position:absolute;top:681px;list-style:none;font-weight:800;font-size:14.5px;line-height:20.5px}
.features li::before{content:"";display:inline-block;width:4px;height:4px;background:var(--white);margin-right:10px;vertical-align:4px}
.features.left{left:220px}.features.right{left:653px}
.footer-line{position:absolute;left:0;top:810px;width:1200px;height:4px;background:var(--footer-line)}
.footer{position:absolute;left:0;top:814px;width:1200px;height:41px;background:var(--footer)}
.copyright{position:absolute;left:190px;top:14px;font-size:9px;font-style:italic;color:var(--copyright)}
</style>
</head>
<body>
<div class="backdrop" role="img" aria-label="Party crowd with raised hands under warm orange and red stage lights"></div>
<div class="topbar"></div>
<div class="navbar"></div>
<div class="brand"><span class="brand-mark"></span><span class="brand-name">Plumtree<br>Gatherings</span></div>
<ul class="menu">
  <li class="current">Home</li><li>About Us</li><li>FAQ</li><li>Order Tickets</li><li>Contact Us</li>
</ul>

<h1 class="headline"><div class="l1">kickoff</div><div class="l2">exclusive <b>vip</b></div><div>july 4<sup>th</sup> party</div></h1>
<svg class="swoosh" width="175" height="50" viewBox="0 0 175 50"><path d="M2 38 Q90 52 172 5 Q100 44 2 38Z" fill="var(--yellow)"/></svg>
<div class="ship" role="img" aria-label="Photo of a lit-up party yacht"></div>

<div class="departure">Departing&nbsp; 9:00 pm, Thursday, July 3, 2014</div>
<div class="perks">OPEN BAR<span>|</span>LUXURY FOOD<span>|</span>GIFT BAGS<span>|</span>LIVE MUSIC</div>
<div class="read-more">read more</div>
<div class="pager"><i></i><i></i><i></i><i></i></div>

<svg class="collage" width="1200" height="855" viewBox="0 0 1200 855">
  <g role="img" aria-label="Photo of a DJ turntable under blue light" transform="rotate(37 545 540)">
    <rect x="475" y="470" width="140" height="140" fill="#1a3aa8" stroke="var(--frame)" stroke-width="12"/>
  </g>
  <g role="img" aria-label="Photo of the city harbor at sunset" transform="rotate(24 722 550)">
    <rect x="654" y="484" width="136" height="132" fill="#5a7fb0" stroke="var(--frame)" stroke-width="12"/>
  </g>
  <g role="img" aria-label="Photo of a singer performing with a guitar" transform="rotate(27 366 583)">
    <rect x="286" y="513" width="160" height="140" fill="#3d2a4a" stroke="var(--frame)" stroke-width="12"/>
  </g>
  <g role="img" aria-label="Photo of a red carpet entrance" transform="rotate(40 615 662)">
    <rect x="548" y="595" width="134" height="134" fill="#e61010" stroke="var(--frame)" stroke-width="12"/>
  </g>
</svg>

<section class="calendar">
  <h3>EVENT CALENDAR</h3>
  <div class="month">July</div>
  <div class="days">
    <span class="head">S</span><span class="head">M</span><span class="head">T</span><span class="head">W</span><span class="head">T</span><span class="head">F</span><span class="head">S</span>
    <span></span><span></span><span>1</span><span>2</span><span>3</span><span><span class="mark">4</span></span><span>5</span>
    <span>6</span><span>7</span><span>8</span><span>9</span><span>10</span><span>11</span><span>12</span>
    <span>13</span><span>14</span><span>15</span><span>16</span><span><span class="mark">17</span></span><span>18</span><span>19</span>
    <span>20</span><span>21</span><span>22</span><span><span class="mark">23</span></span><span>24</span><span>25</span><span>26</span>
    <span>27</span><span>28</span><span>29</span><span>30</span><span>31</span><span></span><span></span>
  </div>
</section>

<ul class="features left">
  <li>Opening Performance by Levi Marsh</li>
  <li>3+ Hour Cruise around NYC Harbor</li>
  <li>Red Carpet Entry</li>
  <li>Epic Mixes by DJ Rivo</li>
</ul>
<ul class="features right">
  <li>Premium Buffet</li>
  <li>Personalized Gift Bag</li>
  <li>Hors d'oeuvres</li>
  <li>Open Premium Bar</li>
</ul>

<div class="footer-line"></div>
<footer class="footer"><p class="copyright">Copyright © Plumtree Gatherings. All rights reserved.</p></footer>
</body>
</html>
```